quorvelbank.com

Design proposals for a gold bank site and gold wallet main page. The site will let people (and companies) open accounts and purchase gold for deposit and later make payments with the gold they hold in the bank. The bank will be a e-money licensed venture located in Switzerland. The functionality of the "system" will be very simple and possibly only use icon symbols so it can be multilingual.

The mainstays of the site will be security and trust. Al digital gold is backed 100 % by visible gold in vault audited every day.

Target Market(s)

Asian and American gold buyers and people preferring gold to currency

Industry/Entity Type

Security

Requirements
Must have
• a) Logo
b) Main index page with a new logo and design
c) System (post log in e-wallet) main page showing the last transactions of the client and give client options to transfer funds and make deposits
Nice to have
• sample contact form
sample faq page
terms page design
Should not have
• So much text since it will be aimed at the worldwide market

```html
<!DOCTYPE html>
<html lang="en">
<head>
<meta charset="utf-8">
<title>QuorvelBank – Account Overview</title>
<link rel="stylesheet" href="https://fonts.googleapis.com/css2?family=Arimo:wght@400;700&display=swap">
<style>
  :root{
    --ink:#1a1a1a;
    --ink-soft:#444;
    --muted:#6b6b6b;
    --gold:#d99a12;
    --gold-dark:#a8741c;
    --gold-light:#efd27a;
    --gold-mid:#e2bc55;
    --bar-dark:#111;
    --bar-mid:#3a3a3a;
    --band:#ececec;
    --line:#d6d6d6;
    --row-alt:#f2f2f2;
    --row:#f9f9f9;
    --white:#fff;
  }
  *{box-sizing:border-box;margin:0;padding:0}
  html,body{width:1200px;height:894px;overflow:hidden}
  body{position:relative;background:var(--white);font-family:"Arimo",Arial,sans-serif;color:var(--ink)}
  a{color:inherit;text-decoration:none}

  .top-bar{position:absolute;left:0;top:0;width:1200px;height:64px;
    background:linear-gradient(90deg,var(--bar-dark),var(--bar-mid) 50%,var(--bar-dark));
    color:var(--white);font-size:14.5px;display:flex;justify-content:space-between;align-items:center;padding:0 30px 2px 42px}
  .top-bar span.sep{margin:0 7px}

  .site-header{position:absolute;left:0;top:64px;width:1200px;height:92px;
    background:linear-gradient(#fff,#ededed);border-bottom:3px solid #dcdcdc}
  .brand{position:absolute;left:40px;top:20px}
  .brand-name{font-size:35px;font-weight:700;color:var(--gold-dark);letter-spacing:1px;line-height:1}
  .brand-tag{margin-top:6px;font-size:11px;letter-spacing:2.4px;color:var(--muted)}

  .welcome-band{position:absolute;left:0;top:158px;width:1200px;height:45px;background:var(--band);
    display:flex;justify-content:space-between;align-items:center;padding:0 34px 0 38px;color:var(--ink-soft)}
  .welcome-band .greet{font-size:24px}
  .welcome-band .acct{font-size:18px}

  .balance{position:absolute;left:40px;top:222px;font-size:25px;color:var(--ink)}
  .balance b{font-weight:400;color:var(--muted)}
  .activity-tabs{position:absolute;left:532px;top:232px;font-size:14px}
  .activity-tabs a.link{color:var(--gold)}

  .activity-panel{position:absolute;left:28px;top:269px;width:823px;height:452px;border:1px solid var(--line);background:var(--row)}
  .panel-head{height:53px;display:flex;justify-content:space-between;align-items:center;padding:0 10px 0 14px;font-size:14px;background:#fafafa}
  .panel-head a{color:var(--gold)}
  .activity-table{width:100%;border-collapse:collapse;font-size:14px}
  .activity-table th{height:36px;text-align:left;font-weight:700;background:linear-gradient(#ececec,#d9d9d9);border-right:1px solid #c9c9c9;padding-left:14px}
  .activity-table th:last-child{border-right:0}
  .activity-table td{height:54px;padding-left:17px}
  .activity-table tr:nth-child(even) td{background:var(--row-alt)}
  .activity-table td.details{color:var(--gold);padding-left:18px}

  .action-card{position:absolute;left:878px;width:292px;height:113px;border-radius:3px;
    background:linear-gradient(var(--gold-light),var(--gold-mid));color:var(--white);border:1px solid #d6ad48}
  .action-card.transfer{top:268px}
  .action-card.deposit{top:406px}
  .action-icon{position:absolute;left:14px;top:42px;width:44px;height:30px;border-radius:6px;background:#d9a94a}
  .action-title{position:absolute;left:72px;top:36px;font-size:19px;font-weight:700;letter-spacing:0;white-space:nowrap}
  .action-sub{position:absolute;left:72px;top:60px;font-size:14px;white-space:nowrap}
  .action-go{position:absolute;right:0;top:21px;width:34px;height:70px;background:#cf9838;display:flex;align-items:center;justify-content:center}

  .security-card{position:absolute;left:878px;top:544px;width:292px;height:136px;border:1px solid #e3e3e3;border-radius:3px;background:#fafafa}
  .badge-placeholder{position:absolute;left:14px;top:16px;width:78px;height:102px;border-radius:4px;
    background:linear-gradient(135deg,#d9a94a,#5a3512)}
  .security-card h3{position:absolute;left:110px;top:22px;font-size:17.5px;font-weight:700}
  .security-card p{position:absolute;left:111px;top:46px;width:170px;font-size:13px;line-height:16px;color:var(--muted)}
  .security-card a{position:absolute;left:111px;top:100px;font-size:13px;font-weight:700;color:var(--gold)}

  .site-footer{position:absolute;left:0;top:755px;width:1200px;height:139px;
    background:linear-gradient(90deg,#222,#3d3d3d 50%,#222);color:var(--white);text-align:center}
  .footer-brand{margin-top:27px;font-size:19px;font-weight:700;color:var(--gold-light);letter-spacing:1px}
  .footer-links{margin-top:12px;font-size:13px}
  .footer-links .sep{margin:0 8px}
  .copyright{margin-top:14px;font-size:12.5px}
</style>
</head>
<body>
  <div class="top-bar">
    <div>Account Type: Personal<span class="sep">|</span>UpgradeStatus: Verified<span class="sep">|</span>Account Limits: View Limits</div>
    <div><a href="#">Log Out</a><span class="sep">|</span><a href="#">Help</a><span class="sep">|</span><a href="#">Security and Protection</a></div>
  </div>

  <header class="site-header">
    <div class="brand">
      <div class="brand-name">QUORVELBANK</div>
      <div class="brand-tag">ONLINE BANKING &amp; MONEY MANAGEMENT</div>
    </div>
  </header>

  <div class="welcome-band">
    <div class="greet">Welcome, Daniel Hart</div>
    <div class="acct">Account I 2367854</div>
  </div>

  <div class="balance"><b>BALANCE:</b> $45,211.58 USD</div>
  <div class="activity-tabs">My recent activity I <a class="link" href="#">Payments sent</a> I <a class="link" href="#">Deposits Made</a></div>

  <section class="activity-panel">
    <div class="panel-head">
      <div><b>My Recent Activity</b> - Last 7 Days (Aug 13, 2012 - Aug 20, 2012)</div>
      <a href="#">View All of my transactions</a>
    </div>
    <table class="activity-table">
      <colgroup><col style="width:150px"><col style="width:88px"><col style="width:105px"><col style="width:157px"><col style="width:173px"><col></colgroup>
      <thead><tr><th>Date</th><th>Type</th><th>Name</th><th>Payment Status</th><th>Details</th><th>Gross</th></tr></thead>
      <tbody>
        <tr><td>Augeust 13,2012</td><td>Transfer</td><td>John Doe</td><td>John Doe</td><td class="details">Details</td><td>$400.00 USD</td></tr>
        <tr><td>Augeust 14,2012</td><td>Transfer</td><td>John Doe</td><td>John Doe</td><td class="details">Details</td><td>$234.00 USD</td></tr>
        <tr><td>Augeust 15,2012</td><td>Transfer</td><td>John Doe</td><td>John Doe</td><td class="details">Details</td><td>$450.00 USD</td></tr>
        <tr><td>Augeust 15,2012</td><td>Transfer</td><td>John Doe</td><td>John Doe</td><td class="details">Details</td><td>$200.00 USD</td></tr>
        <tr><td>Augeust 15,2012</td><td>Transfer</td><td>John Doe</td><td>John Doe</td><td class="details">Details</td><td>$200.00 USD</td></tr>
        <tr><td>Augeust 15,2012</td><td>Transfer</td><td>John Doe</td><td>John Doe</td><td class="details">Details</td><td>$400.00 USD</td></tr>
      </tbody>
    </table>
  </section>

  <a class="action-card transfer" href="#">
    <div class="action-icon" role="img" aria-label="Stack of banknotes icon"></div>
    <div class="action-title">TRANFER FUNDS</div>
    <div class="action-sub">Lorem ipsum dolor sit am</div>
    <div class="action-go"><svg width="16" height="20" viewBox="0 0 16 20"><path d="M4 3l8 7-8 7" fill="none" stroke="#fff" stroke-width="3.5"/></svg></div>
  </a>

  <a class="action-card deposit" href="#">
    <div class="action-icon" role="img" aria-label="Piggy bank icon"></div>
    <div class="action-title">MAKE DEPOSIT</div>
    <div class="action-sub">Lorem ipsum dolor sit am</div>
    <div class="action-go"><svg width="16" height="20" viewBox="0 0 16 20"><path d="M4 3l8 7-8 7" fill="none" stroke="#fff" stroke-width="3.5"/></svg></div>
  </a>

  <aside class="security-card">
    <div class="badge-placeholder" role="img" aria-label="Security emblem"></div>
    <h3>SECURITY</h3>
    <p>Quorvelbank is the most secure way to manage your digital gold</p>
    <a href="#">LEARN MORE</a>
  </aside>

  <footer class="site-footer">
    <div class="footer-brand">QUORVELBANK</div>
    <div class="footer-links">About Us<span class="sep">I</span>Contact Us<span class="sep">I</span>Legal Agreements<span class="sep">I</span>Privacy<span class="sep">I</span>Fees<span class="sep">I</span>Site Feedback</div>
    <div class="copyright">Copyright © 1999-2012 Tellerly. All rights reserved.</div>
  </footer>
</body>
</html>
```